Simple and clean

We need a business card design for a new company called Dwelling Owl. It is a search engine to find current properties for sale or rent in New Zealand market.
We have already a colour scheme that we would like people to use.
Light brown: #D4CCB0
Light green: #D6E4D4
Green: #669966
Black/White
It is OK to divert from this colour scheme slightly as long as there is a green component to the business card.
Final design should be clean, simple and should communicate the nature of the business.
Target Market(s)
- First home buyers
- Real estate agents
- People seeking rentals
Industry/Entity Type
Business
Requirements
Must have
- Use those or similar colours.
Light brown: #D4CCB0
Light green: #D6E4D4
Green: #669966
Black/White

```html
<!DOCTYPE html>
<html lang="en">
<head>
<meta charset="utf-8">
<title>Dwelling Owl – Business Card</title>
<link href="https://fonts.googleapis.com/css2?family=Source+Sans+3:ital,wght@0,400;0,600;0,700;1,400&display=swap" rel="stylesheet">
<style>
  :root {
    --page: #ffffff;
    --ink: #1c1c1c;
    --green: #669966;
    --green-deep: #3f7a3f;
    --green-name: #3b7a3b;
    --light-green: #d6e4d4;
    --light-brown: #e4dcbf;
    --grey-soft: #e2e2e2;
    --grey-text: #5a5a5a;
    --ring: #6f6f6f;
    --card-line: #d8d8d8;
  }
  html, body {
    margin: 0;
    width: 1200px;
    height: 1200px;
    overflow: hidden;
    background: var(--page);
  }
  .canvas {
    position: relative;
    width: 1200px;
    height: 1200px;
  }
  .card {
    position: absolute;
    left: 117px;
    top: 281px;
    width: 938px;
    height: 607px;
    overflow: hidden;
    border: 1px solid var(--card-line);
    box-sizing: border-box;
    background: linear-gradient(to bottom, #ffffff 0, #ffffff 36%, var(--grey-soft) 80%);
    font-family: "Source Sans 3", sans-serif;
  }
  .brand {
    position: absolute;
    left: 24px;
    top: 44px;
    display: flex;
    align-items: center;
    gap: 26px;
  }
  .brand-dot {
    width: 86px;
    height: 86px;
    border-radius: 50%;
    background: var(--green);
  }
  .brand-name {
    font-size: 62px;
    font-weight: 700;
    color: var(--ink);
    letter-spacing: -0.5px;
    line-height: 1;
  }
  .trail {
    position: absolute;
    left: 20px;
    top: 170px;
    width: 920px;
    height: 230px;
    background: linear-gradient(160deg, rgba(214,228,212,0) 10%, rgba(160,196,160,0.35) 55%, rgba(102,153,102,0.45) 100%);
    clip-path: polygon(0 95%, 100% 5%, 100% 30%, 0 100%);
  }
  .footer-band {
    position: absolute;
    left: 0;
    top: 492px;
    width: 100%;
    height: 115px;
    background: var(--green-deep);
  }
  .web {
    position: absolute;
    left: 51px;
    top: 537px;
    font-size: 40px;
    font-weight: 700;
    color: var(--light-brown);
    line-height: 1;
  }
  .lens {
    position: absolute;
    left: 444px;
    top: 159px;
    width: 428px;
    height: 428px;
    box-sizing: border-box;
    border-radius: 50%;
    border: 16px solid var(--ring);
    box-shadow: inset 0 0 0 4px #b9b9b9, 0 4px 10px rgba(0,0,0,0.25);
    background: linear-gradient(to bottom, #f7f7f7 0, #eceeec 76%, #5f9a5f 76%, #4f8a4f 100%);
  }
  .contact {
    position: absolute;
    left: 561px;
    top: 296px;
    color: var(--grey-text);
  }
  .contact-name {
    margin: 0;
    font-size: 34px;
    font-weight: 700;
    color: var(--green-name);
    line-height: 1.1;
  }
  .contact-role {
    margin: 0;
    font-size: 22px;
    font-style: italic;
    color: var(--ink);
    line-height: 1.2;
  }
  .contact-details {
    margin: 26px 0 0;
    font-size: 21px;
    font-weight: 600;
    line-height: 1.4;
  }
</style>
</head>
<body>
<div class="canvas">
  <div class="card">
    <div class="trail" role="img" aria-label="Trail of green footprints crossing the card"></div>
    <div class="footer-band"></div>
    <div class="web">www.dwellingowl.co.nz</div>
    <div class="lens" role="img" aria-label="Large magnifying glass lens framing the contact details"></div>

    <div class="brand">
      <div class="brand-dot"></div>
      <div class="brand-name">Dwelling Owl</div>
    </div>

    <div class="contact">
      <p class="contact-name">Mara TILLS</p>
      <p class="contact-role">Director</p>
      <p class="contact-details">310 482 775<br>mtills@dwellingowl.nz</p>
    </div>
  </div>
</div>
</body>
</html>
```